Velnix Orbit Nine Toothbrush Backcard Design

We need a toothbrush backcard (toothbrush packaging) design for our new toothbrush. We are one of the leading toothbrush distributor and producer company. At the moment our toothbrushes are selling at Varno, Sunpeak Shop, Q-Ninety and many more supermarkets and mom-and-pop shops in Thailand. Our toothbrush is emphasized on the soft and slim tip bristles which will not hurt your enamel. Easy to grip handle that will ease of use. These 2 mains point should be communicated through the design.

Our brand name is Velnix (see attached logo that you can use) and the toothbrush model is Orbit Nine. We will have 2 series for this model which are Orbit Nine Extra Soft and Orbit Nine Medium soft. They are basically differentiated by its packaging colors.

We are looking for the attractive and outstanding design from what available in the market right now. Please see enclosed die cut shape of the packaging. This backcard will hold 3 pieces of toothbrush with clear blister cover.

P.S We are very confident that our product produced with very good quality that's why we want to attract people to try. So when they walk in the aisle we want our toothbrush packaging to be eye catching and welcome customer to try.

Target Market(s)

B+ household consumers age between 18-65 both men and women who has open minded to the new product and willing to spend money without brand royalty.

Font styles to use
Sans Serif

Colors

Designer to choose colors to be used in the design.

Requirements
Must have
• - Logo, and model name
• - Quality mark as following GMP, KRV, ISO9001:2015, ISO22176
• - Attractive character which attract the target clients to try.
• - 2-sided packaging using attached die cut
Nice to have
Should not have
• What other brands have

```html
<!DOCTYPE html>
<html lang="en">
<head>
<meta charset="utf-8">
<title>Velnix Orbit Nine Backcards</title>
<link href="https://fonts.googleapis.com/css2?family=Open+Sans:wght@400;600;700;800&display=swap" rel="stylesheet">
<style>
  :root {
    --stage: #dfe1e7;
    --card: #ffffff;
    --card-edge: #d4d6da;
    --inner-line: #c9cbcf;
    --ink: #1e1e1e;
    --brand-ink: #3b3b3b;
    --gold: #d99a12;
    --product-dark: #1a1a1a;
    --product-mid: #3a3a3a;
    --mono-wave-a: #f1f1f2;
    --color-wave-a: #7fe3e0;
    --color-wave-b: #5a6de6;
    --color-wave-c: #8fe36a;
    --color-wave-d: #f29a5a;
  }
  * { box-sizing: border-box; margin: 0; padding: 0; }
  html, body { width: 1200px; height: 1200px; overflow: hidden; }
  body {
    background: var(--stage);
    font-family: "Open Sans", Arial, sans-serif;
    position: relative;
  }
  .backcard {
    position: absolute;
    top: 179px;
    width: 240px;
    height: 793px;
    background: var(--card);
    border: 1px solid var(--card-edge);
    border-radius: 14px;
    overflow: hidden;
  }
  .backcard--extra { left: 240px; }
  .backcard--medium { left: 696px; }
  .backcard__waves {
    position: absolute;
    inset: 0;
  }
  .backcard--extra .backcard__waves {
    background: linear-gradient(200deg, var(--mono-wave-a) 0%, #ffffff 25%, var(--mono-wave-a) 50%, #e9e9eb 70%, #ffffff 100%);
  }
  .backcard--medium .backcard__waves {
    background:
      linear-gradient(180deg, rgba(255,255,255,0) 0%, rgba(255,255,255,.5) 100%),
      linear-gradient(195deg, var(--color-wave-a) 0%, var(--color-wave-b) 28%, #9be6f0 45%, var(--color-wave-c) 68%, #f2e26a 85%, var(--color-wave-d) 100%);
    opacity: .35;
  }
  .backcard__inner-frame {
    position: absolute;
    top: 10px; left: 10px; right: 10px; bottom: 34px;
    border: 1px solid var(--inner-line);
    border-radius: 10px;
  }
  .backcard__variant {
    position: absolute;
    top: 18px; left: 86px;
    font-size: 10px;
    font-weight: 600;
    color: var(--ink);
    line-height: 12px;
  }
  .backcard__hang-slot {
    position: absolute;
    top: 40px; left: 84px;
    width: 132px; height: 32px;
    border: 1px solid var(--inner-line);
    border-radius: 6px;
    background: rgba(255,255,255,.7);
  }
  .brand-name {
    position: absolute;
    left: 42px;
    top: 215px;
    transform: rotate(-90deg);
    transform-origin: left top;
    font-size: 32px;
    line-height: 36px;
    font-weight: 800;
    color: var(--brand-ink);
    letter-spacing: 1px;
    white-space: nowrap;
  }
  .model-name {
    position: absolute;
    left: 42px;
    top: 719px;
    transform: rotate(-90deg);
    transform-origin: left top;
    font-size: 24px;
    line-height: 28px;
    font-weight: 700;
    color: var(--gold);
    letter-spacing: 4px;
    white-space: nowrap;
  }
  .product-view {
    position: absolute;
    left: 124px;
    top: 108px;
    width: 70px;
    height: 644px;
    border-radius: 12px;
    background: linear-gradient(180deg, var(--product-mid) 0%, var(--product-dark) 50%, var(--product-mid) 100%);
    opacity: .9;
  }
  .quality-marks {
    position: absolute;
    bottom: 12px;
    left: 0; right: 0;
    text-align: center;
    font-size: 9.5px;
    line-height: 12px;
    font-weight: 700;
    color: var(--ink);
  }
</style>
</head>
<body>

<section class="backcard backcard--extra">
  <div class="backcard__waves" role="img" aria-label="Soft grey flowing line pattern"></div>
  <div class="backcard__inner-frame"></div>
  <p class="backcard__variant">EXTRA SOFT</p>
  <div class="backcard__hang-slot"></div>
  <p class="brand-name">Velnix</p>
  <div class="product-view" role="img" aria-label="Black slim toothbrush product photo"></div>
  <p class="model-name">ORBIT NINE</p>
  <p class="quality-marks">GMP, KRV, ISO9001:2015, ISO22176</p>
</section>

<section class="backcard backcard--medium">
  <div class="backcard__waves" role="img" aria-label="Colourful flowing line pattern from blue to green and orange"></div>
  <div class="backcard__inner-frame"></div>
  <p class="backcard__variant">MEDIUM SOFT</p>
  <div class="backcard__hang-slot"></div>
  <p class="brand-name">Velnix</p>
  <div class="product-view" role="img" aria-label="Black slim toothbrush product photo"></div>
  <p class="model-name">ORBIT NINE</p>
  <p class="quality-marks">GMP, KRV, ISO9001:2015, ISO22176</p>
</section>

</body>
</html>
```